Corvane Industries business cards

We need business cards for our company Corvane Industries, based in Brisbane but trading world wide. We buy and sell Corvane Industries, generators and marine equipment. The design needs to be kept clean, simple but eye catching.
Please keep with our current logo (included) and further information can be included on request

Business

0792cd
33a6d7
85cae6
3276b5
0455a3
cedeed
cee9f5
ffffff

```html
<!DOCTYPE html>
<html lang="en">
<head>
<meta charset="utf-8">
<title>Corvane Industries – Business Cards</title>
<link rel="stylesheet" href="https://fonts.googleapis.com/css2?family=Questrial&family=Mulish:wght@700&display=swap">
<style>
  :root {
    --brand: #3276b5;
    --brand-deep: #0455a3;
    --text: #5a5a5a;
    --card: #ffffff;
    --backdrop: #e9edf1;
  }
  * { margin: 0; padding: 0; box-sizing: border-box; }
  html, body { width: 1200px; height: 900px; overflow: hidden; }
  body {
    background: var(--backdrop);
    font-family: "Questrial", sans-serif;
    position: relative;
  }
  .card {
    position: absolute;
    left: 300px;
    width: 600px;
    height: 343px;
    background: var(--card);
    box-shadow: 0 2px 10px rgba(0,0,0,0.08);
  }
  .card--front { top: 90px; }
  .card--back { top: 467px; }

  .brand-lockup {
    position: absolute;
    left: 50%;
    top: 118px;
    transform: translateX(-50%);
    display: flex;
    align-items: center;
    gap: 14px;
  }
  .brand-lockup__square {
    width: 44px; height: 44px;
    background: var(--brand);
    border-radius: 6px;
  }
  .brand-lockup__name {
    font-size: 34px;
    color: var(--brand);
    white-space: nowrap;
  }
  .brand-web {
    position: absolute;
    top: 190px;
    width: 100%;
    text-align: center;
    font-size: 15px;
    color: var(--brand);
    letter-spacing: 0.3px;
  }

  .contact {
    position: absolute;
    left: 48px;
    top: 118px;
    color: var(--text);
  }
  .contact__name {
    font-family: "Mulish", sans-serif;
    font-weight: 700;
    font-size: 22px;
    color: var(--brand);
    margin-bottom: 18px;
  }
  .contact__address {
    font-size: 14px;
    line-height: 21px;
    margin-bottom: 14px;
  }
  .contact__list { list-style: none; font-size: 14px; }
  .contact__item {
    display: flex;
    align-items: center;
    gap: 12px;
    height: 22px;
  }
  .contact__icon { width: 16px; height: 16px; flex: none; }
</style>
</head>
<body>
  <section class="card card--front" aria-label="Card front">
    <div class="brand-lockup">
      <span class="brand-lockup__square"></span>
      <span class="brand-lockup__name">Corvane Industries</span>
    </div>
    <p class="brand-web">www.corvane-industries.com.au</p>
  </section>

  <section class="card card--back" aria-label="Card back">
    <div class="contact">
      <h1 class="contact__name">Marla Quenby</h1>
      <p class="contact__address">18 Tarlow Street, Hemmant QLD 4174<br>PO Box 512, Wynnum<br>QLD 4178</p>
      <ul class="contact__list">
        <li class="contact__item">
          <svg class="contact__icon" viewBox="0 0 16 16" aria-hidden="true"><path d="M2 5c0-2 2-3 6-3s6 1 6 3v1h-3V5H5v1H2z" fill="var(--brand)"/><rect x="4" y="7" width="8" height="7" rx="1" fill="none" stroke="var(--brand)" stroke-width="1.4"/><circle cx="8" cy="10.5" r="1.5" fill="var(--brand)"/></svg>
          <span>+61 7 3000 0142</span>
        </li>
        <li class="contact__item">
          <svg class="contact__icon" viewBox="0 0 16 16" aria-hidden="true"><rect x="4" y="1.5" width="8" height="13" rx="1.5" fill="none" stroke="var(--brand)" stroke-width="1.4"/><circle cx="8" cy="12" r="0.9" fill="var(--brand)"/></svg>
          <span>+61 400 000 218</span>
        </li>
        <li class="contact__item">
          <svg class="contact__icon" viewBox="0 0 16 16" aria-hidden="true"><rect x="4" y="1.5" width="8" height="4" fill="none" stroke="var(--brand)" stroke-width="1.3"/><rect x="1.5" y="6" width="13" height="6" rx="1" fill="var(--brand)"/><rect x="4" y="10" width="8" height="4.5" fill="#fff" stroke="var(--brand)" stroke-width="1.3"/></svg>
          <span>+61 7 3000 0199</span>
        </li>
        <li class="contact__item">
          <svg class="contact__icon" viewBox="0 0 16 16" aria-hidden="true"><rect x="1.5" y="3.5" width="13" height="9" fill="none" stroke="var(--brand)" stroke-width="1.4"/><path d="M1.5 3.5 8 9l6.5-5.5" fill="none" stroke="var(--brand)" stroke-width="1.4"/></svg>
          <span>marla@corvane-industries.com.au</span>
        </li>
      </ul>
    </div>
  </section>
</body>
</html>
```